Minimalistic logo and website for plovrek.com

My colleague and I just started a new company. We need a website to replace the placeholder at https://plovrek.com/

We need a onepager website. A logotype and color profiles. We like minimalism. Scandinavian design.

Below is just information about the company. You can rearrange it, add photos, emit stuff. Maybe even add stuff if you think it is necessary.

# About Plovrek
Plovrek builds critical applications to capture new markets, create modern services and captivate our customers in new and engaging ways. Creating effective and engaging solutions that truly work has always been Plovrek's core offering and is what makes us excited to work in digital. We are a forward thinking company embracing the opportunities of digital transformation and automations.

# Core services
Business automation
Application development and services for desktop and mobile
Interface Design and UX
Enterprise integrations

# Some more data
Plovrek was founded by Torvald Ekblom and Mikael Grundberg in 2021.
Linkedin: https://www.vendalink.com/company/58402917/admin/

# Inspiration
Minimal. Simple.
https://www.kvarnbyformverk.se/contact

Target Market(s)

Businesses

Industry/Entity Type

IT, business automation, data

Number of Pages Required

1 page

Font styles to use
Sans Serif

Colors

Designer to choose colors to be used in the design.

Requirements
Must have
• Onepage design. Minimalism.
Should not have
• Menus

```html
<!DOCTYPE html>
<html lang="en">
<head>
<meta charset="utf-8">
<title>Plovrek — Creative &amp; Clean</title>
<link href="https://fonts.googleapis.com/css2?family=Montserrat:wght@300;400;500;600;700;800&display=swap" rel="stylesheet">
<style>
:root{
  --ink:#0e1621;
  --black:#111214;
  --yellow:#f5b800;
  --white:#ffffff;
  --mist:#f0f1f6;
  --text:#2a2d34;
  --muted:#6b6f78;
  --line:#e2e4ea;
}
*{margin:0;padding:0;box-sizing:border-box}
html,body{width:1200px;height:3080px;overflow:hidden}
body{font-family:'Montserrat',sans-serif;color:var(--text);background:var(--white)}
.section{position:relative;width:1200px;overflow:hidden}
.wrap{position:absolute;left:150px;right:150px;top:0;bottom:0}
.bar{display:block;width:64px;height:6px;background:var(--yellow);margin-bottom:30px}
.heading{font-weight:700;font-size:58px;line-height:1.08;color:var(--ink)}
.body-text{font-size:15px;line-height:1.75;color:var(--muted)}

/* hero */
.hero{height:560px;background:var(--ink)}
.brand{position:absolute;left:0;top:28px;color:var(--white);font-weight:700;font-size:38px;letter-spacing:.5px}
.menu-icon{position:absolute;right:0;top:40px;width:42px}
.menu-icon span{display:block;height:3px;background:var(--white);margin-bottom:7px;border-radius:2px}
.menu-icon span:last-child{width:26px;margin-left:auto}
.hero-title{position:absolute;left:0;top:210px}
.hero-title .heading{color:var(--white);font-size:64px}
.hero-art{position:absolute;left:490px;top:110px;width:460px;height:400px;border-radius:18px;
  background:radial-gradient(circle at 50% 50%,#e9ecf3 0%,#b9c0cf 40%,rgba(14,22,33,0) 72%)}

/* about */
.about{height:340px;background:var(--white)}
.about .title{position:absolute;left:0;top:100px}
.about .body-text{position:absolute;left:390px;top:96px;width:620px}

/* services */
.services{height:580px;background:var(--mist)}
.services .title{position:absolute;left:0;top:100px}
.services .intro{position:absolute;left:0;top:290px;width:250px;font-size:14px}
.service-card{position:absolute;width:240px;height:180px;background:var(--white);border-radius:6px;
  box-shadow:0 4px 18px rgba(14,22,33,.06);text-align:center;padding-top:30px}
.service-card svg{width:64px;height:64px}
.service-card h3{margin-top:16px;font-size:16px;font-weight:700;line-height:1.3;color:var(--ink);text-transform:uppercase}

/* why */
.why{height:280px;background:var(--black)}
.why .title{position:absolute;left:0;top:90px}
.why .heading{color:var(--white)}
.stat{position:absolute;top:82px;text-align:center}
.stat strong{display:block;font-size:64px;font-weight:700;color:var(--white);line-height:1}
.stat span{display:block;margin-top:12px;font-size:16px;color:#9ea3ad}

/* team */
.team{height:440px;background:var(--white)}
.team .title{position:absolute;left:0;top:100px}
.team .intro{position:absolute;left:0;top:214px;width:260px;font-size:14px}
.member{position:absolute;top:80px;width:240px;height:280px;background:var(--white);border-radius:6px;
  box-shadow:0 4px 20px rgba(14,22,33,.1);padding:12px}
.member .photo{height:190px;border-radius:3px}
.member h3{margin-top:16px;font-size:16px;font-weight:600;text-align:center;color:var(--ink)}
.member .social{display:flex;justify-content:center;gap:10px;margin-top:10px}
.member .social i{width:12px;height:12px;background:var(--ink);border-radius:2px}

/* partners */
.partners{height:540px;background:var(--mist)}
.partners .title{position:absolute;left:0;top:90px}
.partners .body-text{position:absolute;left:410px;top:146px;width:490px;font-size:14px}
.partner-grid{position:absolute;left:0;top:232px;width:900px;display:grid;grid-template-columns:repeat(6,130px);gap:32px 24px}
.partner{height:88px;background:var(--white);border-radius:4px;display:flex;align-items:center;justify-content:center}
.partner i{width:66px;height:20px;background:#c9ccd4;border-radius:3px}

/* footer */
.footer{height:340px;background:var(--black);color:var(--white)}
.cta{position:absolute;left:0;top:72px;font-size:28px;line-height:1.25;text-transform:uppercase}
.cta b{font-weight:700;display:block}
.cta span{font-weight:300}
.subscribe{position:absolute;right:0;top:84px;display:flex}
.subscribe .field{width:318px;height:42px;background:var(--white);color:#8a8e96;font-size:13px;padding:13px 14px}
.subscribe .btn{width:122px;height:42px;background:var(--yellow);color:var(--ink);font-weight:700;font-size:13px;
  text-align:center;line-height:42px;text-transform:uppercase}
.socials{position:absolute;left:0;right:0;top:184px;display:flex;justify-content:center;gap:14px}
.socials i{width:34px;height:34px;border-radius:50%;background:var(--white)}
.rule{position:absolute;left:0;right:0;top:248px;height:1px;background:#3a3d44}
.links{position:absolute;left:0;right:0;top:268px;text-align:center;font-size:13px}
.links span{margin:0 14px}
.copyright{position:absolute;left:0;right:0;top:302px;text-align:center;font-size:12px;color:#c8cbd1}
</style>
</head>
<body>

<section class="section hero">
  <div class="wrap">
    <div class="brand">Plovrek</div>
    <div class="menu-icon"><span></span><span></span><span></span></div>
    <div class="hero-title">
      <span class="bar"></span>
      <h1 class="heading">Creative &amp;<br>Clean</h1>
    </div>
    <div class="hero-art" role="img" aria-label="Illustration of app screens, charts and interface cards floating around a laptop"></div>
  </div>
</section>

<section class="section about">
  <div class="wrap">
    <div class="title">
      <span class="bar"></span>
      <h2 class="heading">About<br>Plovrek</h2>
    </div>
    <p class="body-text">Plovrek builds critical applications to capture new markets, create modern services and captivate our customers in new and engaging ways. Creating effective and engaging solutions that truly work has always been Plovrek's core offering and is what makes us excited to work in digital. We are a forward thinking company embracing the opportunities of digital transformation and automations.</p>
  </div>
</section>

<section class="section services">
  <div class="wrap">
    <div class="title">
      <span class="bar"></span>
      <h2 class="heading">Core<br>Services</h2>
    </div>
    <p class="body-text intro">We are a forward thinking company embracing the opportunities of digital transformation and automations.</p>

    <div class="service-card" style="left:394px;top:100px">
      <svg viewBox="0 0 64 64" fill="none" stroke="#0e1621" stroke-width="2.5"><rect x="14" y="8" width="36" height="48" rx="3"/><path d="M22 22h20M22 32h20M22 42h12"/><circle cx="44" cy="44" r="8"/></svg>
      <h3>Business<br>Automation</h3>
    </div>
    <div class="service-card" style="left:666px;top:100px">
      <svg viewBox="0 0 64 64" fill="none" stroke="#0e1621" stroke-width="2.5"><rect x="8" y="12" width="40" height="28" rx="3"/><path d="M20 48h16M28 40v8"/><rect x="42" y="24" width="14" height="26" rx="2"/></svg>
      <h3>App Development<br>and Services</h3>
    </div>
    <div class="service-card" style="left:394px;top:320px">
      <svg viewBox="0 0 64 64" fill="none" stroke="#0e1621" stroke-width="2.5"><circle cx="32" cy="32" r="12"/><circle cx="32" cy="32" r="4"/><path d="M32 8v8M32 48v8M8 32h8M48 32h8M15 15l6 6M43 43l6 6M15 49l6-6M43 21l6-6"/></svg>
      <h3>Interface Design<br>and UX</h3>
    </div>
    <div class="service-card" style="left:666px;top:320px">
      <svg viewBox="0 0 64 64" fill="none" stroke="#0e1621" stroke-width="2.5"><circle cx="24" cy="26" r="10"/><circle cx="42" cy="40" r="10"/><path d="M24 10v6M24 36v6M8 26h6M34 26h6M42 24v6M42 50v6M26 40h6M52 40h6"/></svg>
      <h3>Enterprise<br>Integrations</h3>
    </div>
  </div>
</section>

<section class="section why">
  <div class="wrap">
    <div class="title">
      <span class="bar"></span>
      <h2 class="heading">Why Us?</h2>
    </div>
    <div class="stat" style="left:400px"><strong>556</strong><span>Projects</span></div>
    <div class="stat" style="left:596px"><strong>450</strong><span>Happy Clients</span></div>
    <div class="stat" style="left:812px"><strong>25</strong><span>Awards</span></div>
  </div>
</section>

<section class="section team">
  <div class="wrap">
    <div class="title">
      <span class="bar"></span>
      <h2 class="heading">Our Team</h2>
    </div>
    <p class="body-text intro">Plovrek was founded by Torvald Ekblom and Mikael Grundberg in 2021.</p>

    <div class="member" style="left:394px">
      <div class="photo" role="img" aria-label="Portrait photo of Torvald Ekblom" style="background:linear-gradient(160deg,#8a8f96,#3d4147)"></div>
      <h3>Torvald Ekblom</h3>
      <div class="social"><i></i><i></i><i></i></div>
    </div>
    <div class="member" style="left:666px">
      <div class="photo" role="img" aria-label="Portrait photo of Mikael Grundberg" style="background:linear-gradient(160deg,#c9b49c,#7d6a58)"></div>
      <h3>Mikael Grundberg</h3>
      <div class="social"><i></i><i></i><i></i></div>
    </div>
  </div>
</section>

<section class="section partners">
  <div class="wrap">
    <div class="title">
      <span class="bar"></span>
      <h2 class="heading">Partners</h2>
    </div>
    <p class="body-text">We are a forward thinking company embracing the opportunities of digital transformation and automations.</p>
    <div class="partner-grid">
      <div class="partner"><i></i></div><div class="partner"><i></i></div><div class="partner"><i></i></div>
      <div class="partner"><i></i></div><div class="partner"><i></i></div><div class="partner"><i></i></div>
      <div class="partner"><i></i></div><div class="partner"><i></i></div><div class="partner"><i></i></div>
      <div class="partner"><i></i></div><div class="partner"><i></i></div><div class="partner"><i></i></div>
    </div>
  </div>
</section>

<footer class="section footer">
  <div class="wrap">
    <div class="cta"><span>Want to know about us</span><b>Join our community</b></div>
    <div class="subscribe"><div class="field">Email Address</div><div class="btn">Subscribe</div></div>
    <div class="socials"><i></i><i></i><i></i><i></i></div>
    <div class="rule"></div>
    <div class="links"><span>Home</span>|<span>About us</span>|<span>Our Services</span>|<span>Partners</span>|<span>Contact Us</span>|<span>Privacy Policy</span></div>
    <div class="copyright">Copyright © 2023 Plovrek. All Rights Reserved.</div>
  </div>
</footer>

</body>
</html>
```